Business Card Design Project

Business Card
We are rebranding with a new logo
Industry/Entity Type
Business
Contact Information for Business Card
Dennis Marlow +61 427581962 dennis@qovo.com.au P.O. Box 872 Kelvindale QLD 4309
Requirements
Must have
- Logo

```html
<!DOCTYPE html>
<html lang="en">
<head>
<meta charset="utf-8">
<title>Qovo International – Business Card</title>
<link rel="stylesheet" href="https://fonts.googleapis.com/css2?family=Open+Sans:wght@400;600;700&display=swap">
<style>
  :root {
    --backdrop: #2a2829;
    --card-white: #ffffff;
    --brand-blue: #0a84b6;
    --brand-blue-deep: #0d5f94;
    --accent-orange: #f28a1c;
    --ink: #0f1a26;
  }
  * { margin: 0; padding: 0; box-sizing: border-box; }
  html, body {
    width: 1200px; height: 716px; overflow: hidden;
    background: var(--backdrop);
    font-family: "Open Sans", Arial, sans-serif;
  }
  .card {
    position: absolute; left: 180px; top: 103px;
    width: 840px; height: 510px;
    background: var(--card-white);
    overflow: hidden;
    box-shadow: 0 14px 40px rgba(0,0,0,.45);
  }
  .card-shapes { position: absolute; inset: 0; }
  .brand {
    position: absolute; left: 0; right: 0; top: 190px;
    display: flex; align-items: center; justify-content: center; gap: 16px;
  }
  .brand-dot {
    width: 34px; height: 34px; border-radius: 50%;
    background: var(--brand-blue);
  }
  .brand-name {
    font-weight: 700; font-size: 46px; letter-spacing: 1px;
    color: var(--brand-blue-deep);
  }
  .holder {
    position: absolute; left: 64px; top: 372px;
    font-size: 18px; font-weight: 600; color: var(--ink);
  }
  .holder-rule {
    position: absolute; left: 0; top: 402px;
    width: 200px; height: 2px; background: var(--accent-orange);
  }
  .contact {
    position: absolute; left: 520px; top: 388px;
    list-style: none; color: var(--ink); font-size: 15px;
  }
  .contact li { display: flex; align-items: center; gap: 9px; line-height: 26px; }
  .contact li.address { margin-top: 8px; }
  .contact svg { width: 14px; height: 14px; flex: none; }
</style>
</head>
<body>
  <div class="card">
    <svg class="card-shapes" viewBox="0 0 840 510" width="840" height="510">
      <path d="M0 0 H840 V44 Q420 4 0 16 Z" fill="var(--brand-blue)"/>
      <path d="M0 22 Q420 10 840 50" fill="none" stroke="var(--accent-orange)" stroke-width="2"/>
      <path d="M0 346 Q420 378 840 334 V510 H0 Z" fill="var(--brand-blue)"/>
      <path d="M0 342 Q420 374 840 330" fill="none" stroke="var(--accent-orange)" stroke-width="3"/>
    </svg>

    <div class="brand">
      <span class="brand-dot"></span>
      <span class="brand-name">Qovo International</span>
    </div>

    <div class="holder">Dennis Marlow</div>
    <div class="holder-rule"></div>

    <ul class="contact">
      <li>
        <svg viewBox="0 0 24 24"><path fill="var(--ink)" d="M6.6 10.8a15 15 0 0 0 6.6 6.6l2.2-2.2c.3-.3.7-.4 1-.2 1.1.4 2.3.6 3.6.6.6 0 1 .4 1 1V20c0 .6-.4 1-1 1A17 17 0 0 1 3 4c0-.6.4-1 1-1h3.5c.6 0 1 .4 1 1 0 1.3.2 2.5.6 3.6.1.3 0 .7-.2 1z"/></svg>
        +61 427581962
      </li>
      <li>
        <svg viewBox="0 0 24 24"><rect x="2" y="5" width="20" height="14" fill="none" stroke="var(--ink)" stroke-width="2"/><path d="M2 6l10 7 10-7" fill="none" stroke="var(--ink)" stroke-width="2"/></svg>
        dennis@qovo.com.au
      </li>
      <li class="address">
        <svg viewBox="0 0 24 24"><path fill="var(--ink)" d="M12 2a7 7 0 0 0-7 7c0 5 7 13 7 13s7-8 7-13a7 7 0 0 0-7-7zm0 9.5A2.5 2.5 0 1 1 12 6.5a2.5 2.5 0 0 1 0 5z"/></svg>
        P.O. Box 872 Kelvindale QLD 4309
      </li>
    </ul>
  </div>
</body>
</html>
```